MRC New Busines Card

we need a business card for or renovation company, our main color is orange and our logo is a concrete ball rolling with MRC on it.the company name is Maple Ridge Contractors, Inc, we need somthing simple but profecional, also that we can change if its for roofing or renovations and the names

Target Market(s)

home owners

Industry/Entity Type

Concrete

Contact Information for Business Card

.

Colors
f68d4d
f9ba93
f37122
f78f20
faa54b
fbc994

```html
<!DOCTYPE html>
<html lang="en">
<head>
<meta charset="utf-8">
<title>Maple Ridge Contractors – Business Card</title>
<link rel="stylesheet" href="https://fonts.googleapis.com/css2?family=Roboto+Condensed:wght@400;700&family=Arimo:wght@400;700&display=swap">
<style>
  :root {
    --page: #e8e5e0;
    --card-black: #0b0b0b;
    --card-white: #ffffff;
    --gold: #f7a823;
    --gold-deep: #d98a12;
    --ink: #1e1e1e;
    --muted: #c4c4c4;
    --mark-grey: #b9b2a8;
    --text-light: #ffffff;
  }
  html, body {
    margin: 0;
    padding: 0;
    width: 1200px;
    height: 892px;
    overflow: hidden;
    background: var(--page);
  }
  .business-card {
    position: absolute;
    left: 75px;
    top: 146px;
    width: 1050px;
    height: 600px;
    background: var(--card-black);
    overflow: hidden;
    box-shadow: 0 10px 30px rgba(0,0,0,0.25);
    font-family: "Arimo", Arial, sans-serif;
  }
  .card-shapes {
    position: absolute;
    inset: 0;
  }
  .services-line {
    position: absolute;
    left: 70px;
    top: 300px;
    transform: translate(-50%, -50%) rotate(-90deg);
    white-space: nowrap;
    font-size: 27px;
    letter-spacing: 1.5px;
    color: var(--muted);
  }
  .brand {
    position: absolute;
    left: 150px;
    top: 120px;
    width: 380px;
  }
  .brand-mark {
    display: flex;
    align-items: center;
    justify-content: flex-end;
    gap: 14px;
    margin-right: 40px;
  }
  .brand-mark .dot {
    width: 90px;
    height: 90px;
    border-radius: 50%;
    background: var(--mark-grey);
  }
  .brand-mark .initials {
    font-family: "Roboto Condensed", Arial, sans-serif;
    font-weight: 700;
    font-size: 38px;
    color: var(--ink);
  }
  .brand-name {
    margin: 20px 0 0;
    font-family: "Roboto Condensed", Arial, sans-serif;
    font-weight: 700;
    font-size: 54px;
    line-height: 1;
    color: var(--ink);
    letter-spacing: -0.5px;
    white-space: nowrap;
  }
  .brand-suffix {
    margin: 8px 0 0;
    font-family: "Roboto Condensed", Arial, sans-serif;
    font-weight: 700;
    font-size: 34px;
    line-height: 1;
    color: var(--ink);
    letter-spacing: 1px;
    white-space: nowrap;
  }
  .contact {
    position: absolute;
    right: 50px;
    text-align: right;
    color: var(--text-light);
    font-size: 24px;
    line-height: 1.45;
    white-space: nowrap;
  }
  .contact-top { top: 110px; }
  .contact-bottom { top: 335px; }
  .phone-main {
    color: var(--gold);
    font-size: 44px;
    line-height: 1.2;
    margin-bottom: 8px;
  }
  .tagline {
    color: var(--gold);
    margin-top: 14px;
    font-size: 25px;
  }
</style>
</head>
<body>
  <div class="business-card">
    <svg class="card-shapes" width="1050" height="600" viewBox="0 0 1050 600" aria-hidden="true">
      <defs>
        <linearGradient id="goldBand" x1="0" y1="0" x2="0" y2="1">
          <stop offset="0" stop-color="#f9c54a"/>
          <stop offset="0.5" stop-color="#f7a823"/>
          <stop offset="1" stop-color="#d98a12"/>
        </linearGradient>
      </defs>
      <circle cx="-20" cy="180" r="578" fill="url(#goldBand)"/>
      <circle cx="-20" cy="180" r="566" fill="#0b0b0b"/>
      <circle cx="-20" cy="180" r="560" fill="#ffffff"/>
      <rect x="535" y="297" width="515" height="6" fill="#f7a823"/>
    </svg>

    <div class="services-line">Roofing . Painting . Renovations</div>

    <div class="brand">
      <div class="brand-mark">
        <span class="dot"></span>
        <span class="initials">MRC</span>
      </div>
      <p class="brand-name">Maple Ridge</p>
      <p class="brand-suffix">Contractors, Inc</p>
    </div>

    <div class="contact contact-top">
      <div class="phone-main">(555)-310-4827</div>
      <div>1420 Cedar Hollow Ln</div>
      <div>Fairview, GA 30000</div>
    </div>

    <div class="contact contact-bottom">
      <div>(555)-672-1938</div>
      <div>www.mapleridgecontractors.com</div>
      <div>info@MapleRidgeContractors.com</div>
      <div class="tagline">“Solid Work For Every Home, Every Season”</div>
    </div>
  </div>
</body>
</html>
```